Family Day Care Educator Diary 2014 COVER - Amaze us

We need a printable diary cover design for an Australian not-for-profit organisation that supports Family Day Care. Family Day Care is form of child care where children receive quality education and care from an educator in the educator's own home.

Educators have to comply with many national laws and regulations and documenting and reporting is a very important aspect of this. To assist them with this we publish a yearly diary.

We are looking for a full colour cover design for our 2014 Educator Diary.
Please refer to the attached design from previous years.

More information about the Association can be found on our website:
www.kbrtmlo.org.au

Target Market(s)

Most women, age range 30-60

Industry/Entity Type

Education

Requirements
Must have
• - KBRTMLO logo, TOLV logo, BMZ logo, social media logo, phone numbers, large colour photo(s). A4 size. Landscape lay-out.
Nice to have
• - Modern look and feel. Also original. Can be playful. Not a standard font.
Should not have
• - Not too corporate please

```html
<!DOCTYPE html>
<html lang="en">
<head>
<meta charset="utf-8">
<title>Educator Diary 2014 Cover</title>
<link href="https://fonts.googleapis.com/css2?family=Bebas+Neue&family=Oswald:wght@500;700&family=Dancing+Script:wght@700&display=swap" rel="stylesheet">
<style>
  :root {
    --sky: #6ccbf2;
    --green: #3cb44a;
    --pink: #ee6fb0;
    --magenta: #e6157f;
    --ink: #1d2733;
    --lavender: #dfe3f4;
    --note-yellow: #fdf3a6;
    --note-peach: #f9c8c9;
    --pin: #f3f3f3;
    --purple: #6b3a8e;
    --orange: #f26a21;
    --grey-ink: #222;
  }
  * { margin: 0; padding: 0; box-sizing: border-box; }
  html, body { width: 1200px; height: 849px; overflow: hidden; background: #fff; }
  .cover { position: relative; width: 1200px; height: 849px; background: var(--green); overflow: hidden; font-family: "Oswald", sans-serif; }

  .title-panel { position: absolute; left: 0; top: 0; width: 831px; height: 365px; background: var(--sky); }
  .photo-panel { position: absolute; left: 0; top: 377px; width: 831px; height: 472px; background: #fff; }
  .side-panel { position: absolute; left: 843px; top: 0; width: 357px; height: 849px; background: var(--pink); }

  .org-line { position: absolute; left: 140px; top: 30px; font-family: "Oswald", sans-serif; font-weight: 700; font-size: 46px; letter-spacing: 1px; line-height: 1; }
  .org-line .w1 { color: var(--purple); }
  .org-line .w2 { color: var(--orange); }
  .org-line .w3 { color: var(--green); }
  .org-line .w4 { color: var(--purple); }

  .diary-title { position: absolute; left: 140px; top: 92px; font-family: "Bebas Neue", sans-serif; font-weight: 400; color: var(--ink); line-height: 0.92; }
  .diary-title .educator { display: block; font-size: 142px; letter-spacing: 6px; }
  .diary-title .diary { display: inline-block; font-size: 142px; letter-spacing: 6px; }
  .diary-title .year { display: inline-block; margin-left: 26px; font-family: "Oswald", sans-serif; font-weight: 500; font-size: 122px; color: var(--magenta); letter-spacing: 3px; }

  .photo { position: absolute; left: 40px; top: 10px; width: 740px; height: 452px; background: radial-gradient(ellipse 60% 55% at 48% 55%, #a9cf7f 0%, #f4d35a 35%, #f0a24a 60%, rgba(255,255,255,0) 100%); }

  .note { position: absolute; display: flex; flex-direction: column; align-items: center; padding-bottom: 18px; box-shadow: 2px 3px 6px rgba(0,0,0,0.18); }
  .note::before { content: ""; position: absolute; top: -10px; left: 50%; width: 16px; height: 22px; margin-left: -8px; background: var(--pin); box-shadow: 1px 1px 2px rgba(0,0,0,0.2); }
  .note-association { left: 94px; top: 51px; width: 188px; height: 189px; background: var(--lavender); transform: rotate(-1deg); }
  .note-backing { position: absolute; left: 62px; top: 300px; width: 250px; height: 168px; background: var(--note-peach); transform: rotate(3deg); }
  .note-service { left: 42px; top: 291px; width: 258px; height: 176px; background: var(--note-yellow); transform: rotate(-2deg);
    background-image: repeating-linear-gradient(to bottom, transparent 0 22px, rgba(214,170,100,0.35) 22px 23px); }
  .note-training { left: 94px; top: 514px; width: 204px; height: 190px; background: var(--lavender); transform: rotate(1deg); }

  .brand { display: flex; align-items: center; gap: 10px; margin-top: 38px; margin-bottom: auto; font-family: "Oswald", sans-serif; font-weight: 700; font-size: 30px; line-height: 1; color: var(--purple); letter-spacing: 1px; }
  .brand-dot { width: 22px; height: 22px; border-radius: 50%; background: var(--purple); }
  .phone { font-family: "Oswald", sans-serif; font-weight: 700; font-size: 22px; line-height: 1; color: var(--grey-ink); letter-spacing: 1px; }

  .follow { position: absolute; left: 86px; top: 738px; width: 260px; }
  .follow-label { font-family: "Dancing Script", cursive; font-weight: 700; font-size: 32px; line-height: 1.1; color: var(--ink); }
  .social-list { display: flex; gap: 9px; margin-top: 8px; font-family: "Oswald", sans-serif; font-weight: 500; font-size: 15px; line-height: 1; color: var(--ink); }
</style>
</head>
<body>
<div class="cover">
  <section class="title-panel">
    <h2 class="org-line"><span class="w1">KBRTMLO</span> <span class="w2">FAMILY</span> <span class="w3">DAY</span> <span class="w4">CARE</span></h2>
    <h1 class="diary-title">
      <span class="educator">EDUCATOR</span>
      <span class="diary">DIARY</span><span class="year">2014</span>
    </h1>
  </section>

  <section class="photo-panel">
    <div class="photo" role="img" aria-label="Photo of five young children sitting on the floor around a potted plant on a toy wagon, watering it"></div>
  </section>

  <aside class="side-panel">
    <div class="note note-association">
      <div class="brand"><span class="brand-dot"></span>KBRTMLO</div>
      <p class="phone">1800 402 615</p>
    </div>
    <div class="note-backing"></div>
    <div class="note note-service">
      <div class="brand"><span class="brand-dot"></span>BMZ</div>
      <p class="phone">1300 648 209</p>
    </div>
    <div class="note note-training">
      <div class="brand"><span class="brand-dot"></span>TOLV</div>
      <p class="phone">9381 2706</p>
    </div>
    <div class="follow">
      <p class="follow-label">follow us on</p>
      <p class="social-list"><span>Chatterly</span><span>Pinstack</span><span>Tweetle</span><span>Clipcast</span></p>
    </div>
  </aside>
</div>
</body>
</html>
```